Card Design for my dog training business RB Paws Training

Need a business card design for my dog training business with my new logo. Want the card to come off professional yet fun. Want it to be very eye catchy as well. I normally have these at vet clinics, pet stores, and groomers. so need it to look better than my competitors.
Target Market(s)
dog owners
Industry/Entity Type
Dog Training
Contact Information for Business Card
needs logo, my name and info
Font styles to use
Serif
Colors
0255a3
ffffff
ec1f27
000000
333333
fbfbfb
Requirements
Must have
- RB Paws Training
- Lydia Fensworth
- 555 390 2176
- info@rbpawstraining.example
- www.rbpawstraining.example

```html
<!DOCTYPE html>
<html lang="en">
<head>
<meta charset="utf-8">
<title>RB Paws Training – Business Card</title>
<link rel="stylesheet" href="https://fonts.googleapis.com/css2?family=Cormorant+Garamond:ital,wght@0,500;0,600;1,500&family=Lato:wght@400;600&display=swap">
<style>
  :root {
    --backdrop: #1c1c1c;
    --card: #1f1f1f;
    --card-edge: #2a2a2a;
    --white: #fbfbfb;
    --red: #ec1f27;
    --orange-red: #f0552a;
    --muted: #d9d9d9;
  }
  * { box-sizing: border-box; margin: 0; padding: 0; }
  html, body {
    width: 1200px; height: 900px; overflow: hidden;
    background: var(--backdrop);
  }
  .canvas {
    width: 1200px; height: 900px;
    display: flex; flex-direction: column; align-items: center; justify-content: center;
    gap: 44px;
  }
  .card {
    position: relative;
    width: 720px; height: 400px;
    background: linear-gradient(135deg, var(--card) 0%, var(--card-edge) 100%);
    box-shadow: 0 10px 30px rgba(0,0,0,.5);
    overflow: hidden;
  }
  .card::after {
    content: ""; position: absolute; left: 0; right: 0; bottom: 0; height: 5px;
    background: var(--red);
  }
  .card--front::after { background: var(--orange-red); }

  .wordmark {
    font-family: "Lato", sans-serif; font-weight: 600;
    color: var(--white); letter-spacing: .06em;
    text-transform: uppercase;
  }
  .card--front .wordmark {
    position: absolute; top: 50%; left: 50%; transform: translate(-50%, -50%);
    font-size: 34px; white-space: nowrap;
  }

  .brand-block {
    position: absolute; left: 40px; top: 0; bottom: 0; width: 300px;
    display: flex; flex-direction: column; align-items: center; justify-content: center; gap: 18px;
  }
  .brand-block .wordmark { font-size: 26px; white-space: nowrap; }
  .tagline {
    font-family: "Cormorant Garamond", serif; font-style: italic; font-weight: 500;
    font-size: 14px; color: var(--white);
  }
  .divider {
    position: absolute; left: 368px; top: 90px; width: 2px; height: 200px;
    background: var(--red);
  }
  .contact {
    position: absolute; left: 400px; top: 88px;
    font-family: "Lato", sans-serif; color: var(--white);
  }
  .contact__name {
    font-family: "Cormorant Garamond", serif; font-weight: 600;
    font-size: 26px; color: var(--red); text-transform: uppercase; letter-spacing: .03em;
  }
  .contact__role { font-size: 20px; margin-top: 2px; }
  .contact__address { font-size: 20px; line-height: 1.3; margin-top: 14px; }
  .contact__list { list-style: none; margin-top: 8px; }
  .contact__item { display: flex; align-items: center; gap: 10px; font-size: 20px; line-height: 1.45; }
  .contact__icon { width: 14px; height: 14px; flex: none; }
</style>
</head>
<body>
<main class="canvas">
  <section class="card card--front" aria-label="Card front">
    <div class="wordmark">RB Paws Training</div>
  </section>

  <section class="card card--back" aria-label="Card back">
    <div class="brand-block">
      <div class="wordmark">RB Paws Training</div>
      <p class="tagline">“Training dogs across Texas one dog at a time.”</p>
    </div>
    <div class="divider"></div>
    <div class="contact">
      <h1 class="contact__name">Lydia Fensworth</h1>
      <p class="contact__role">Managing Director</p>
      <p class="contact__address">48 Alder Row,<br>Brookvale, 70412</p>
      <ul class="contact__list">
        <li class="contact__item">
          <svg class="contact__icon" viewBox="0 0 24 24" fill="none" stroke="#ec1f27" stroke-width="2.4" stroke-linecap="round"><path d="M5 3h4l2 5-2.5 1.5a11 11 0 0 0 6 6L16 13l5 2v4a2 2 0 0 1-2 2A17 17 0 0 1 3 5a2 2 0 0 1 2-2z"/></svg>
          555 390 2176
        </li>
        <li class="contact__item">
          <svg class="contact__icon" viewBox="0 0 24 24" fill="none" stroke="#ec1f27" stroke-width="2.4"><rect x="3" y="5" width="18" height="14" rx="1"/><path d="M3 6l9 7 9-7"/></svg>
          info@rbpawstraining.example
        </li>
        <li class="contact__item">
          <svg class="contact__icon" viewBox="0 0 24 24" fill="none" stroke="#ec1f27" stroke-width="2.2"><circle cx="12" cy="12" r="9"/><path d="M3 12h18M12 3c3 3 3 15 0 18M12 3c-3 3-3 15 0 18"/></svg>
          www.rbpawstraining.example
        </li>
      </ul>
    </div>
  </section>
</main>
</body>
</html>
```